Rack card

Design double sided rack card. Please see our website for current information. www.beaconorbitlink.com

Please see attachment of previous rack card

```html
<!DOCTYPE html>
<html lang="en">
<head>
<meta charset="utf-8">
<title>Beacon Orbit Link – Ultra Services Rack Card</title>
<link rel="stylesheet" href="https://fonts.googleapis.com/css2?family=Oswald:wght@500;600&family=Roboto+Slab:wght@400;500;600&display=swap">
<style>
  :root {
    --navy: #0b3f78;
    --navy-deep: #07264c;
    --ring-blue: #0a5bb5;
    --bright-blue: #1e8ff0;
    --inner-blue: #16559c;
    --grey-ring: #dcdcdc;
    --ink: #111418;
    --body-ink: #333;
    --red: #c4101b;
    --dot-red: #e8202a;
    --white: #ffffff;
  }
  * { margin: 0; padding: 0; box-sizing: border-box; }
  html, body { width: 1200px; height: 2550px; overflow: hidden; }
  body { position: relative; font-family: "Roboto Slab", serif; background: var(--navy-deep); }

  .sky {
    position: absolute; inset: 0;
    background:
      radial-gradient(ellipse 600px 400px at 300px 1950px, rgba(70,140,230,.45), transparent 70%),
      linear-gradient(180deg, #0c4a8a 20%, #0b3f7a 55%, #0a3266 78%, #06203f 100%);
  }
  .mountains {
    position: absolute; left: 0; right: 0; top: 2060px; height: 490px;
    background: linear-gradient(180deg, rgba(8,35,70,0) 0%, rgba(7,30,62,.85) 30%, #061c3a 100%);
  }
  .top-panel { position: absolute; left: 0; top: 0; width: 1200px; height: 900px; }

  .section-title {
    position: absolute; left: 0; width: 1200px; text-align: center;
    font-family: "Oswald", sans-serif; font-weight: 600; font-size: 62px; letter-spacing: .5px;
  }
  .section-title.dark { color: var(--ink); top: 52px; }
  .section-title.light { color: var(--white); top: 1175px; }

  .ring { position: absolute; }

  .plan-name {
    position: absolute; font-family: "Oswald", sans-serif; font-weight: 500;
    font-size: 38px; color: var(--ink);
  }
  .bullets { position: absolute; list-style: none; }
  .bullets li { position: relative; padding-left: 25px; margin-bottom: 11px; }
  .bullets li::before {
    content: ""; position: absolute; left: 2px; top: 8px;
    border-left: 12px solid var(--ring-blue);
    border-top: 10px solid transparent; border-bottom: 10px solid transparent;
  }
  .bullets.ultra { font-size: 25px; line-height: 37px; color: var(--body-ink); width: 500px; }
  .bullets.gen { font-size: 25px; line-height: 37px; color: var(--white); font-weight: 600; width: 300px; }
  .bullets.gen li { margin-bottom: 8px; }
  .bullets.gen li::before { border-left-color: var(--white); border-left-width: 9px; border-top-width: 8px; border-bottom-width: 8px; top: 11px; left: 0; }

  .satellite {
    position: absolute; left: 850px; top: 640px; width: 310px; height: 210px; border-radius: 40% 50%;
    background: radial-gradient(ellipse at 50% 55%, #e8edf3 0%, #b7c3d3 25%, #3a74d6 45%, rgba(40,90,200,.0) 72%);
  }
  .red-dot { position: absolute; left: 227px; top: 793px; width: 64px; height: 64px; border-radius: 50%; background: var(--dot-red); }

  .perk {
    position: absolute; top: 885px; width: 250px; height: 250px; border: 2px solid var(--white);
    border-radius: 50%; color: var(--white); text-align: center;
    font-weight: 600; font-size: 26px; line-height: 33px;
  }
  .perk svg { display: block; margin: 48px auto 0; }
  .perk p { margin-top: 6px; }

  .gen-name {
    position: absolute; left: 258px; font-family: "Oswald", sans-serif; font-weight: 600;
    font-size: 40px; line-height: 46px; color: var(--white);
  }

  .vip { position: absolute; left: 309px; top: 2218px; width: 582px; color: var(--white); text-align: center; }
  .vip h2 { font-family: "Oswald", sans-serif; font-weight: 500; font-size: 42px; line-height: 50px; margin-bottom: 8px; }
  .vip li { list-style: none; font-size: 20px; line-height: 32px; border-bottom: 1px solid rgba(255,255,255,.85); }
  .vip li:last-child { border-bottom: 0; }

  .contact-pill {
    position: absolute; top: 2430px; height: 80px; border-radius: 40px; background: var(--red); color: var(--white);
  }
  .contact-pill.call { left: 197px; width: 402px; }
  .contact-pill.web { left: 605px; width: 400px; }
  .divider { position: absolute; left: 599px; top: 2432px; width: 2px; height: 76px; background: var(--white); }
  .icon-disc { position: absolute; top: 13px; width: 54px; height: 54px; border-radius: 50%; background: var(--white); }
  .call .icon-disc { left: 341px; }
  .web .icon-disc { left: 6px; }
  .icon-disc svg { position: absolute; left: 13px; top: 13px; }
  .call-label { position: absolute; right: 72px; top: 15px; text-align: right; }
  .call-label small { display: block; font-size: 15px; line-height: 16px; }
  .call-label strong { display: block; font-family: "Roboto", "Roboto Slab", sans-serif; font-size: 26px; line-height: 32px; font-weight: 600; }
  .web-label { position: absolute; left: 66px; top: 24px; font-size: 15px; line-height: 25px; font-family: "Times New Roman", serif; }
</style>
</head>
<body>
  <div class="sky" role="img" aria-label="Starry deep-blue night sky"></div>
  <div class="mountains" role="img" aria-label="Silhouetted mountain peaks under the night sky"></div>

  <svg class="top-panel" viewBox="0 0 1200 900" aria-hidden="true">
    <path d="M0 520 Q600 1160 1200 520 V560 Q600 1160 0 560 Z" fill="var(--bright-blue)"/>
    <path d="M0 0 H1200 V545 Q600 1135 0 545 Z" fill="var(--white)"/>
    <line x1="340" y1="139" x2="860" y2="139" stroke="#c9ced6" stroke-width="1.5"/>
    <path d="M578 139 H622 L600 161 Z" fill="var(--ring-blue)"/>
  </svg>

  <h1 class="section-title dark">OUR ULTRA SERVICES</h1>

  <!-- Ultra 100 -->
  <svg class="ring" style="left:250px;top:198px" width="270" height="250" viewBox="0 0 270 250" aria-hidden="true">
    <path d="M240 113 L265 125 L240 137 Z" fill="var(--ring-blue)"/>
    <circle cx="125" cy="125" r="105" fill="none" stroke="var(--ring-blue)" stroke-width="30"/>
    <circle cx="125" cy="125" r="90" fill="var(--white)"/>
    <text x="125" y="116" text-anchor="middle" font-family="Roboto Slab, serif" font-size="24" fill="#222">$119.99</text>
    <text x="125" y="147" text-anchor="middle" font-family="Roboto Slab, serif" font-size="25" font-weight="600" fill="#222">100MBPS</text>
  </svg>
  <h3 class="plan-name" style="left:533px;top:216px">ULTRA 100</h3>
  <ul class="bullets ultra" style="left:533px;top:267px">
    <li>Stream in 4K or stream multiple devices in HD</li>
    <li>Excellent choice for mission critical gaming Ultra low latency, symmetrical speeds. Static IP included</li>
  </ul>

  <!-- Ultra 50 -->
  <svg class="ring" style="left:250px;top:468px" width="270" height="250" viewBox="0 0 270 250" aria-hidden="true">
    <path d="M240 113 L265 125 L240 137 Z" fill="var(--grey-ring)"/>
    <circle cx="125" cy="125" r="105" fill="none" stroke="var(--grey-ring)" stroke-width="30"/>
    <path d="M125 20 A105 105 0 0 0 125 230" fill="none" stroke="var(--ring-blue)" stroke-width="30"/>
    <circle cx="125" cy="125" r="90" fill="var(--white)"/>
    <text x="125" y="116" text-anchor="middle" font-family="Roboto Slab, serif" font-size="24" fill="#222">$159.99</text>
    <text x="125" y="147" text-anchor="middle" font-family="Roboto Slab, serif" font-size="25" font-weight="600" fill="#222">50MBPS</text>
  </svg>
  <h3 class="plan-name" style="left:533px;top:507px">ULTRA 50</h3>
  <ul class="bullets ultra" style="left:533px;top:560px;width:340px">
    <li>Excellent for large households</li>
    <li>Stream, Game in HD with speed to spare</li>
  </ul>

  <div class="satellite" role="img" aria-label="Illustration of a communications satellite with solar panels"></div>
  <div class="red-dot"></div>

  <!-- Perks -->
  <div class="perk" style="left:225px">
    <svg width="56" height="56" viewBox="0 0 56 56" fill="none" stroke="#fff" stroke-width="2.5" stroke-linecap="round" stroke-linejoin="round" aria-hidden="true">
      <path d="M8 48 L34 22 M14 52 L40 26 M34 22 L40 26"/>
      <path d="M38 6 a10 10 0 0 0 12 12 l-6 6 -8-8 z"/>
      <path d="M6 8 l6-2 28 28 4 14 -14-4 -28-28 z"/>
    </svg>
    <p>FREE<br>EQUIPMENTS</p>
  </div>
  <div class="perk" style="left:486px">
    <svg width="66" height="66" viewBox="0 0 66 66" fill="none" stroke="#fff" stroke-width="2.5" stroke-linecap="round" stroke-linejoin="round" aria-hidden="true">
      <path d="M28 4 h10 l2 8 6 3 7-4 7 7 -4 7 3 6 8 2 v10 l-8 2 -3 6 4 7 -7 7 -7-4 -6 3 -2 8 h-10 l-2-8 -6-3 -7 4 -7-7 4-7 -3-6 -8-2 v-10 l8-2 3-6 -4-7 7-7 7 4 6-3 z" transform="scale(0.92) translate(3 3)"/>
      <circle cx="33" cy="33" r="14"/>
      <path d="M26 33 l5 5 9-10"/>
    </svg>
    <p>FREE<br>INSTALLATION</p>
  </div>
  <div class="perk" style="left:749px">
    <svg width="58" height="56" viewBox="0 0 58 56" fill="none" stroke="#fff" stroke-width="2.2" aria-hidden="true">
      <rect x="3" y="8" width="52" height="45" rx="2"/>
      <line x1="3" y1="18" x2="55" y2="18"/>
      <path d="M14 3 v10 M29 3 v10 M44 3 v10"/>
      <g>
        <rect x="9" y="23" width="8" height="6"/><rect x="20" y="23" width="8" height="6"/><rect x="31" y="23" width="8" height="6"/><rect x="42" y="23" width="8" height="6"/>
        <rect x="9" y="33" width="8" height="6"/><rect x="20" y="33" width="8" height="6"/><rect x="31" y="33" width="8" height="6"/><rect x="42" y="33" width="8" height="6"/>
        <rect x="9" y="43" width="8" height="6"/><rect x="20" y="43" width="8" height="6"/><rect x="31" y="43" width="8" height="6"/><rect x="42" y="43" width="8" height="6"/>
      </g>
    </svg>
    <p>FREE<br>FRIST MONTH</p>
  </div>

  <h2 class="section-title light">GEN 5 SPEEDS</h2>
  <svg class="ring" style="left:0;top:1255px" width="1200" height="30" viewBox="0 0 1200 30" aria-hidden="true">
    <line x1="340" y1="6" x2="860" y2="6" stroke="rgba(255,255,255,.45)" stroke-width="1.5"/>
    <path d="M578 6 H622 L600 28 Z" fill="var(--white)"/>
  </svg>

  <!-- Gen5 -->
  <h3 class="gen-name" style="top:1408px">GEN5</h3>
  <svg class="ring" style="left:475px;top:1313px" width="270" height="250" viewBox="0 0 270 250" aria-hidden="true">
    <path d="M240 113 L265 125 L240 137 Z" fill="var(--white)"/>
    <circle cx="125" cy="125" r="105" fill="none" stroke="var(--white)" stroke-width="30"/>
    <path d="M20 125 A105 105 0 0 1 125 20" fill="none" stroke="var(--bright-blue)" stroke-width="30"/>
    <circle cx="125" cy="125" r="90" fill="var(--inner-blue)"/>
    <text x="125" y="116" text-anchor="middle" font-family="Roboto Slab, serif" font-size="24" fill="#fff">$99.99</text>
    <text x="125" y="147" text-anchor="middle" font-family="Roboto Slab, serif" font-size="25" font-weight="600" fill="#fff">15MBPS</text>
  </svg>
  <ul class="bullets gen" style="left:760px;top:1343px">
    <li>SD Streaming on up to two devices</li>
    <li>Basic gaming</li>
    <li>Great for a small household</li>
  </ul>

  <!-- Gen5 Extreme -->
  <h3 class="gen-name" style="top:1661px">GEN5<br>EXTREME</h3>
  <svg class="ring" style="left:475px;top:1573px" width="270" height="250" viewBox="0 0 270 250" aria-hidden="true">
    <path d="M240 113 L265 125 L240 137 Z" fill="var(--white)"/>
    <circle cx="125" cy="125" r="105" fill="none" stroke="var(--white)" stroke-width="30"/>
    <path d="M125 20 A105 105 0 0 0 125 230" fill="none" stroke="var(--bright-blue)" stroke-width="30"/>
    <circle cx="125" cy="125" r="90" fill="var(--inner-blue)"/>
    <text x="125" y="116" text-anchor="middle" font-family="Roboto Slab, serif" font-size="24" fill="#fff">$119.99</text>
    <text x="125" y="147" text-anchor="middle" font-family="Roboto Slab, serif" font-size="25" font-weight="600" fill="#fff">20MBPS</text>
  </svg>
  <ul class="bullets gen" style="left:760px;top:1621px;width:300px">
    <li>Basic HD streaming</li>
    <li>Good for most gaming</li>
    <li>Perfect for mid sized households</li>
  </ul>

  <!-- Gen5 Ultimate -->
  <h3 class="gen-name" style="top:1919px">GEN5<br>ULTIMATE</h3>
  <svg class="ring" style="left:475px;top:1835px" width="270" height="250" viewBox="0 0 270 250" aria-hidden="true">
    <path d="M125 20 A105 105 0 1 0 230 125" fill="none" stroke="var(--bright-blue)" stroke-width="30"/>
    <path d="M125 20 A105 105 0 0 1 230 125" fill="none" stroke="var(--white)" stroke-width="30"/>
    <path d="M240 113 L265 125 L240 137 Z" fill="var(--white)"/>
    <circle cx="125" cy="125" r="90" fill="var(--inner-blue)"/>
    <text x="125" y="116" text-anchor="middle" font-family="Roboto Slab, serif" font-size="24" fill="#fff">$139.99</text>
    <text x="125" y="147" text-anchor="middle" font-family="Roboto Slab, serif" font-size="25" font-weight="600" fill="#fff">25MBPS</text>
  </svg>
  <ul class="bullets gen" style="left:760px;top:1869px;width:300px">
    <li>HD streaming</li>
    <li>Great for gaming</li>
    <li>Excellent for larger households</li>
  </ul>

  <!-- VIP -->
  <section class="vip">
    <h2>NEW VIP SERVICE</h2>
    <ul>
      <li>Tailor a bandwidth pakage to suit your needs</li>
      <li>Customize download and upload speeds</li>
      <li>Choose dedicated or non dedicated service</li>
      <li>Add static ip addressing</li>
    </ul>
  </section>

  <!-- Contact -->
  <div class="contact-pill call">
    <div class="call-label"><small>CALL NOW</small><strong>907-555-0148</strong></div>
    <div class="icon-disc">
      <svg width="28" height="28" viewBox="0 0 24 24" aria-hidden="true"><path fill="#1a1a1a" d="M6.6 10.8a15.1 15.1 0 0 0 6.6 6.6l2.2-2.2c.3-.3.7-.4 1-.2 1.1.4 2.3.6 3.6.6.6 0 1 .4 1 1V20c0 .6-.4 1-1 1A17 17 0 0 1 3 4c0-.6.4-1 1-1h3.5c.6 0 1 .4 1 1 0 1.3.2 2.5.6 3.6.1.3 0 .7-.2 1z" transform="scale(.85) translate(2 2)"/></svg>
    </div>
  </div>
  <div class="divider"></div>
  <div class="contact-pill web">
    <div class="icon-disc">
      <svg width="28" height="28" viewBox="0 0 28 28" fill="none" stroke="#1a1a1a" stroke-width="1.8" aria-hidden="true">
        <circle cx="14" cy="14" r="12"/><ellipse cx="14" cy="14" rx="5" ry="12"/><path d="M2 14h24M4 8h20M4 20h20"/>
      </svg>
    </div>
    <div class="web-label">WWW.BEACONORBITLINK.COM<br>218 W HARBOR VIEW RD SELDON,AK 99650</div>
  </div>
</body>
</html>
```